One Page Website for Personal Trainer in London

I have a logo and need a one page website designed around my branding. I am a freelance Personal Trainer based in London specialising in bodyweight training for men and women. I would like the site to be modern and clean but not overtly urban in design.
I need the following headings:
About Me
My Services
Events
Blog
I don't need them to be seperate pages but if they can link to further down the page that would be great.
Industry/Entity Type
Personal Trainer
Coding
Coded - Design and coding required
Number of Pages Required
1 page
Requirements
Must have
- I need the following headings:
- About Me
- My Services
- Events
- Blog
- mobile friendly formatting
- health and fitness related photography
- Colour scheme in keeping with my existing logo

```html
<!DOCTYPE html>
<html lang="en">
<head>
<meta charset="utf-8">
<title>Marlow Fitness – Personal Trainer London</title>
<link href="https://fonts.googleapis.com/css2?family=Open+Sans:wght@400;600;700;800&display=swap" rel="stylesheet">
<style>
:root{
  --orange:#f7941d;
  --dark:#1f1f1f;
  --darker:#141414;
  --text:#444;
  --muted:#888;
  --light:#f2f2f2;
  --white:#fff;
}
*{margin:0;padding:0;box-sizing:border-box}
html,body{width:1200px;height:3196px;overflow:hidden}
body{font-family:'Open Sans',Arial,sans-serif;color:var(--text);background:var(--white);position:relative}
.abs{position:absolute}
.section-title{font-weight:800;font-size:40px;color:#222;text-align:center;letter-spacing:1px;text-transform:uppercase}
.btn{display:inline-block;background:var(--orange);color:#fff;font-weight:700;font-size:14px;letter-spacing:1px;text-transform:uppercase;padding:0;width:168px;height:54px;line-height:54px;text-align:center}
p.body{font-size:17px;line-height:28px;color:#555}

/* Hero */
.hero{left:0;top:0;width:1200px;height:660px;background:linear-gradient(135deg,#3c4a2c 0%,#5f6f3a 35%,#7d8a52 55%,#4d5e33 75%,#2d3a22 100%)}
.hero-shade{left:0;top:0;width:1200px;height:660px;background:linear-gradient(180deg,rgba(0,0,0,.35),rgba(0,0,0,.1) 40%,rgba(0,0,0,.25))}
.brand{left:120px;top:28px;display:flex;align-items:center;gap:12px;color:#fff;font-weight:700;font-size:22px}
.brand-mark{width:34px;height:34px;border:3px solid #fff}
.nav{right:110px;top:58px;display:flex;gap:44px;font-size:14px;font-weight:700;color:#fff;text-transform:uppercase}
.nav .active{color:var(--orange)}
.hero-title{left:0;top:270px;width:1200px;text-align:center;color:#fff;font-weight:800;font-size:58px;letter-spacing:1px}
.hero-sub{left:250px;top:345px;width:700px;text-align:center;color:#fff;font-weight:700;font-size:20px;line-height:30px}
.dots{left:572px;top:492px;display:flex;gap:10px}
.dots span{width:10px;height:10px;border-radius:50%;background:rgba(255,255,255,.6)}
.dots span.on{background:#fff}

/* About */
.about-photo{left:72px;top:608px;width:516px;height:424px;background:linear-gradient(180deg,#8aa3b4 0%,#c9b59a 55%,#b48f6a 100%)}
.about-title{left:626px;top:722px;font-weight:800;font-size:44px;color:#222;letter-spacing:1px}
.about-text{left:626px;top:800px;width:500px}
.about-btn{left:626px;top:970px}

/* Services */
.services{left:0;top:1080px;width:1200px;height:520px;background:var(--light)}
.services .section-title{position:absolute;left:0;top:90px;width:1200px}
.service{top:164px;width:330px;height:268px;padding:50px 30px 0;text-align:center}
.service h3{color:var(--orange);font-size:15px;font-weight:800;text-transform:uppercase;margin-bottom:10px}
.service p{color:#fff;font-size:13px;line-height:20px}
.s1{left:72px;background:linear-gradient(160deg,#4a3a38,#6d5248 60%,#2c2322)}
.s2{left:432px;background:linear-gradient(160deg,#3a3d44,#5c6068 60%,#25272b)}
.s3{left:792px;background:linear-gradient(160deg,#33302e,#5a544e 60%,#201e1c)}

/* Events */
.events-photo{left:612px;top:1560px;width:508px;height:480px;background:linear-gradient(160deg,#e6e8ea 0%,#c9ced3 40%,#8c939a 75%,#3f4246 100%)}
.events-title{left:72px;top:1706px;font-weight:800;font-size:40px;color:#222;letter-spacing:1px}
.arrows{left:520px;top:1716px;display:flex;gap:18px}
.event-date{left:72px;top:1772px;color:var(--orange);font-weight:700;font-size:14px}
.event-name{left:72px;top:1800px;font-weight:700;font-size:19px;color:#222}
.event-text{left:72px;top:1838px;width:500px}
.events-btn{left:72px;top:1984px}

/* Blog */
.blog{left:0;top:2120px;width:1200px;height:600px;background:#f7f7f7}
.blog .section-title{position:absolute;left:0;top:60px;width:1200px}
.post{top:140px;width:330px}
.post .thumb{width:330px;height:190px}
.post h4{font-size:18px;font-weight:700;color:#222;margin-top:20px}
.post .meta{font-size:12px;color:var(--orange);margin-top:6px}
.post p{font-size:13px;line-height:20px;color:#666;margin-top:8px}
.post .more{font-size:13px;font-weight:700;color:var(--orange);margin-top:8px}
.p1{left:72px}.p2{left:432px}.p3{left:792px}
.t1{background:linear-gradient(135deg,#d9dcd2,#b7b9a8 50%,#8b8d7c)}
.t2{background:linear-gradient(135deg,#c8d2db,#d67b3c 50%,#b83c2e)}
.t3{background:linear-gradient(135deg,#eceae6,#d9463a 55%,#c0362c)}

/* Contact */
.contact{left:0;top:2720px;width:1200px;height:400px;background:var(--dark)}
.contact .section-title{position:absolute;left:0;top:36px;width:1200px;color:#fff}
.field{background:#fff;height:38px;font-size:13px;color:#999;padding:10px 14px}
.f1{left:256px;top:94px;width:336px}
.f2{left:608px;top:94px;width:336px}
.f3{left:256px;top:146px;width:336px}
.f4{left:608px;top:146px;width:336px}
.f5{left:256px;top:198px;width:688px;height:86px}
.submit{left:516px;top:300px;width:168px;height:50px;line-height:50px}
.footer{left:0;top:3120px;width:1200px;height:76px;background:var(--darker)}
.copy{left:72px;top:30px;font-size:12px;color:#888}
.social{left:900px;top:26px;display:flex;gap:18px}
.social span{width:22px;height:22px;border-radius:50%;background:#777}
.top-link{left:1130px;top:28px;color:var(--orange);font-size:13px;font-weight:700}
</style>
</head>
<body>

<header>
  <div class="abs hero" role="img" aria-label="Photo of a personal trainer coaching a woman with suspension straps in a park"></div>
  <div class="abs hero-shade"></div>
  <div class="abs brand"><span class="brand-mark"></span>Marlow Fitness</div>
  <nav class="abs nav">
    <span class="active">Home</span><span>About Me</span><span>My Services</span><span>Events</span><span>Blog</span><span>Contact</span>
  </nav>
  <h1 class="abs hero-title">WELCOME TO MY WEBSITE</h1>
  <p class="abs hero-sub">I am a freelance Personal Trainer based in London specialising in bodyweight training for men and women.</p>
  <div class="abs dots"><span class="on"></span><span></span><span></span><span></span></div>
</header>

<section id="about">
  <div class="abs about-photo" role="img" aria-label="Photo of a woman walking on a beach"></div>
  <h2 class="abs about-title">ABOUT ME</h2>
  <p class="abs body about-text">Aliquam molestie, mi et imperdiet euismod, dui purus auctor tellus, id interdum lacus lectus et ante. Sed accumsan sollicitudin sapien, sit amet adipiscing turpis gravida ac. In congue, eget posuere lobortis volutpat, libero mauris cursus sed nisi.</p>
  <span class="abs btn about-btn">Read More</span>
</section>

<section id="services">
  <div class="abs services">
    <h2 class="section-title">MY SERVICES</h2>
    <div class="abs service s1" role="img" aria-label="Photo of a bodyweight training class">
      <h3>Bodyweight Training</h3>
      <p>Aliquam molestie mi et imperdiet euismod dui purus auctor tellus id interdum lacus.</p>
    </div>
    <div class="abs service s2" role="img" aria-label="Photo of a man training in a gym">
      <h3>Body Weight For Men</h3>
      <p>Aliquam molestie mi et imperdiet euismod dui purus auctor tellus id interdum lacus.</p>
    </div>
    <div class="abs service s3" role="img" aria-label="Photo of a woman training in a gym">
      <h3>Body Weight For Women</h3>
      <p>Aliquam molestie mi et imperdiet euismod dui purus auctor tellus id interdum lacus.</p>
    </div>
  </div>
</section>

<section id="events">
  <div class="abs events-photo" role="img" aria-label="Photo of a group fitness class stretching in a bright studio"></div>
  <h2 class="abs events-title">EVENTS</h2>
  <div class="abs arrows">
    <svg width="14" height="22" viewBox="0 0 14 22"><path d="M11 2 L3 11 L11 20" fill="none" stroke="#555" stroke-width="2.5"/></svg>
    <svg width="14" height="22" viewBox="0 0 14 22"><path d="M3 2 L11 11 L3 20" fill="none" stroke="#555" stroke-width="2.5"/></svg>
  </div>
  <span class="abs event-date">OCT 20, 2017</span>
  <h3 class="abs event-name">Aliquam molestie mi et imperdiet euismod</h3>
  <p class="abs body event-text">Sed accumsan sollicitudin sapien, sit amet adipiscing turpis gravida ac. In congue, eget posuere lobortis volutpat, libero mauris cursus sed nisi. Sed ligula vitae risus lobortis mauris, at interdum lorem.</p>
  <span class="abs btn events-btn">Read More</span>
</section>

<section id="blog">
  <div class="abs blog">
    <h2 class="section-title">BLOG</h2>
    <article class="abs post p1">
      <div class="thumb t1" role="img" aria-label="Photo of a woman doing a floor exercise"></div>
      <h4>Aliquam molestie miet...</h4>
      <div class="meta">Oct 20, 2017 &nbsp;|&nbsp; By Admin</div>
      <p>Sed accumsan sollicitudin sapien, sit amet adipiscing turpis gravida ac in congue eget lobortis.</p>
      <div class="more">Read More</div>
    </article>
    <article class="abs post p2">
      <div class="thumb t2" role="img" aria-label="Photo of a group class with exercise balls"></div>
      <h4>Aliquam molestie miet...</h4>
      <div class="meta">Oct 20, 2017 &nbsp;|&nbsp; By Admin</div>
      <p>Sed accumsan sollicitudin sapien, sit amet adipiscing turpis gravida ac in congue eget lobortis.</p>
      <div class="more">Read More</div>
    </article>
    <article class="abs post p3">
      <div class="thumb t3" role="img" aria-label="Photo of women exercising on red fitness balls"></div>
      <h4>Aliquam molestie miet...</h4>
      <div class="meta">Oct 20, 2017 &nbsp;|&nbsp; By Admin</div>
      <p>Sed accumsan sollicitudin sapien, sit amet adipiscing turpis gravida ac in congue eget lobortis.</p>
      <div class="more">Read More</div>
    </article>
  </div>
</section>

<section id="contact">
  <div class="abs contact">
    <h2 class="section-title">CONTACT</h2>
    <div class="abs field f1">Enter Name</div>
    <div class="abs field f2">Enter Email Address</div>
    <div class="abs field f3">Phone No.</div>
    <div class="abs field f4">Subject</div>
    <div class="abs field f5">Message</div>
    <span class="abs btn submit">Submit</span>
  </div>
</section>

<footer class="abs footer">
  <span class="abs copy">Copyright © 2017 | Marlow Fitness | All Rights Reserved</span>
  <div class="abs social"><span></span><span></span><span></span><span></span><span></span><span></span></div>
  <span class="abs top-link">Top</span>
</footer>

</body>
</html>
```